Cards for Employees

We are looking for an Anniversary and a Birthday card to send to our employees. 2 designs.
We send these cards to our employees based on number of years they work at the company.
Check out our website for more info.
www.BrightfoldServices.example
Target Market(s)
Our Employees -
Font styles to use
Sans Serif
Colors
Designer to choose colors to be used in the design.
Requirements
Must have
- Anniversary card - appreciation for hard work and dedication
Logo - no changes

```html
<!DOCTYPE html>
<html lang="en">
<head>
<meta charset="utf-8">
<title>Brightfold Services – Anniversary Card</title>
<link rel="stylesheet" href="https://fonts.googleapis.com/css2?family=Great+Vibes&family=Montserrat:wght@400;700&display=swap">
<style>
  :root {
    --page-bg: #e6e6e8;
    --frame-blue: #1631a8;
    --accent-red: #e5202e;
    --ink-blue: #3c4fa8;
    --muted-grey: #6a6f86;
    --satin-light: #ffffff;
    --satin-mid: #ececef;
    --satin-shade: #d4d5da;
  }
  * { box-sizing: border-box; margin: 0; padding: 0; }
  html, body {
    width: 1200px;
    height: 2608px;
    overflow: hidden;
    background: var(--page-bg);
  }
  .sheet {
    position: relative;
    width: 1200px;
    height: 2608px;
    display: flex;
    flex-direction: column;
    align-items: center;
    justify-content: center;
    gap: 180px;
  }
  .card {
    position: relative;
    width: 960px;
    height: 700px;
    background: var(--frame-blue);
    padding: 22px;
    box-shadow: 0 18px 40px rgba(0,0,0,0.25);
  }
  .card__inner {
    position: relative;
    width: 100%;
    height: 100%;
    border: 8px solid var(--satin-light);
    overflow: hidden;
  }
  .card__satin {
    position: absolute;
    inset: 0;
    background:
      radial-gradient(ellipse 70% 30% at 30% 70%, var(--satin-shade), transparent 70%),
      radial-gradient(ellipse 60% 25% at 75% 30%, var(--satin-shade), transparent 70%),
      linear-gradient(160deg, var(--satin-light) 0%, var(--satin-mid) 45%, var(--satin-light) 70%, var(--satin-mid) 100%);
  }
  .card__rule {
    position: absolute;
    inset: 10px;
    border: 2px solid var(--accent-red);
    opacity: 0.55;
  }
  .brand-name {
    position: absolute;
    font-family: "Montserrat", sans-serif;
    font-weight: 700;
    color: var(--accent-red);
    text-transform: uppercase;
    text-align: center;
    line-height: 1.05;
  }
  .card--front .brand-name {
    top: 40px;
    left: 50%;
    transform: translateX(-50%);
    font-size: 38px;
  }
  .card--back .brand-name {
    right: 44px;
    bottom: 44px;
    font-size: 30px;
  }
  .greeting {
    position: absolute;
    top: 150px;
    left: 0;
    right: 0;
    text-align: center;
  }
  .greeting__lead {
    position: absolute;
    left: 110px;
    top: 60px;
    font-family: "Great Vibes", cursive;
    font-size: 40px;
    color: var(--ink-blue);
  }
  .greeting__title {
    font-family: "Great Vibes", cursive;
    color: var(--accent-red);
    font-size: 150px;
    line-height: 1.05;
    font-weight: 400;
  }
  .greeting__message {
    position: absolute;
    left: 0;
    right: 0;
    bottom: 64px;
    text-align: center;
    font-family: "Montserrat", sans-serif;
    font-size: 24px;
    letter-spacing: 1px;
    color: var(--muted-grey);
    text-transform: uppercase;
  }
  .greeting__message em {
    font-style: normal;
    color: var(--accent-red);
  }
  .greeting__message::before {
    content: "";
    display: block;
    width: 720px;
    height: 2px;
    margin: 0 auto 12px;
    background: var(--accent-red);
    opacity: 0.4;
  }
</style>
</head>
<body>
  <main class="sheet">
    <section class="card card--front">
      <div class="card__inner">
        <div class="card__satin" role="img" aria-label="Soft white satin fabric background"></div>
        <div class="card__rule"></div>
        <p class="brand-name">Brightfold<br>Services</p>
        <div class="greeting">
          <span class="greeting__lead">Wishing you</span>
          <h1 class="greeting__title">Happy<br>Anniversary</h1>
        </div>
        <p class="greeting__message">Appreciation for <em>hard work</em> and <em>dedication</em></p>
      </div>
    </section>

    <section class="card card--back">
      <div class="card__inner">
        <div class="card__satin" role="img" aria-label="Soft white satin fabric background"></div>
        <div class="card__rule"></div>
        <p class="brand-name">Brightfold<br>Services</p>
      </div>
    </section>
  </main>
</body>
</html>
```